Card Design Project

We are looking for a couple card / box designs that will for a new company that is in the bereavement assistance industry.
Our customers are churches, counseling centers and funeral homes.
Once we have these card designs we will need to work with that same artist to help us out with box graphic designs that are similar to the card designs. The box is 12" long x 4" wide x 6" high
We will need more designs in the future so we are looking for an artist for future work.
Our look needs to be professional and solemn.
The front of the card should be quite close to what i am attaching but with some professional touches to it that give it a proper look. We dont want you to stray to far from what i have attached but if you feel you have some good ideas we would be more than happy to see them.
The back of the card we want people to be able to leave the family a note so will need wording such as "leave a message to the family" or "write a memory"
Keep in mind we will need this look to be able to match graphics on the box as well, we kind of need the card design and box design to go together.
Thanks
Just wanted to mention to all designers that although we would like our logo on the card it is something that we need to keep kind of in the background somehow. We cant be seen as trying to push a brand name too much so please keep that in mind. Thanks
Reason: HOLIDAY
Designers, I took the need to see what the design looked like on a box out.
Reason: just need a bit of extra time guys, thanks for all who are helping us on this!
Target Market(s)
Funeral homes, churches, counseling centers
Industry/Entity Type
Industry
Requirements
Must have
- Professional and solemn look
Card need to be 4"wide X 6" high and needs to be portrait
A pin will be attached to the top right part of the card so will need a space there for it.
I was thinking that we would have the pic of the ribbon symbol there so when the pin is off the card there would still be a ribbon pic there. The pins that we will be attaching are ribbon pins similar to what i have on my pdf's
Please keep in mind that we cant really have out logo in a dominant area on the card. We would like to have it subtly in there but not to where it is in your face type of thing.
Nice to have
- Our logo but very small, not to intrusive .
Would like 2 designs, one dark and another light.
Maybe 1 masculine or gender neutral and another feminine
Wording should be the same

```html
<!DOCTYPE html>
<html lang="en">
<head>
<meta charset="utf-8">
<title>Memorial Pin Card — Front and Back</title>
<link href="https://fonts.googleapis.com/css2?family=Pinyon+Script&display=swap" rel="stylesheet">
<style>
  :root {
    --page: #ffffff;
    --card-edge: #8a8a8a;
    --paper: #fbfaf8;
    --ink: #2a2622;
    --wash-warm-a: #ece5db;
    --wash-warm-b: #d8cbb8;
    --wash-cool-a: #f4f3f1;
    --wash-cool-b: #e3e1dd;
    --rule: #8f8a84;
    --ribbon: #a3a3a3;
    --mark: #bdbbb8;
  }
  * { margin: 0; padding: 0; box-sizing: border-box; }
  html, body { width: 900px; height: 1200px; overflow: hidden; background: var(--page); }
  .canvas { position: relative; width: 900px; height: 1200px; background: var(--page); }

  .card {
    position: absolute; top: 28px; width: 371px; height: 556px;
    border: 1px solid var(--card-edge); background: var(--paper); overflow: hidden;
  }
  .card--front { left: 70px; }
  .card--back { left: 459px; }

  .wash { position: absolute; inset: 0; }
  .wash--warm { background: linear-gradient(160deg, var(--wash-warm-a) 0%, var(--wash-warm-b) 50%, var(--wash-warm-a) 100%); }
  .wash--cool { background: linear-gradient(160deg, var(--wash-cool-b) 0%, var(--wash-cool-a) 55%, var(--wash-cool-b) 100%); }

  .pin-spot {
    position: absolute; left: 302px; top: 26px; width: 40px; height: 72px;
    border-radius: 20px 20px 6px 6px; background: var(--ribbon);
  }

  .letter {
    position: absolute; left: 37px; top: 206px;
    font-family: "Pinyon Script", cursive; font-size: 15px; line-height: 20px;
    color: var(--ink); white-space: nowrap;
  }
  .letter p { margin-bottom: 20px; }

  .maker {
    position: absolute; display: flex; align-items: center; gap: 6px;
    font-family: "Pinyon Script", cursive; font-weight: 400; color: var(--ink); white-space: nowrap;
  }
  .maker__mark { background: var(--mark); flex: none; }
  .card--front .maker { right: 12px; top: 500px; font-size: 13px; }
  .card--front .maker__mark { width: 14px; height: 14px; }
  .card--back .maker { left: 0; right: 0; top: 500px; justify-content: center; font-size: 19px; }
  .card--back .maker__mark { width: 24px; height: 24px; }

  .message__title {
    position: absolute; top: 88px; left: 0; right: 0; text-align: center;
    font-family: "Pinyon Script", cursive; font-weight: 400; font-size: 15px; color: var(--ink);
  }
  .message__lines { position: absolute; left: 45px; top: 113px; width: 282px; }
  .message__line { height: 40px; border-bottom: 1px dotted var(--rule); }
</style>
</head>
<body>
<main class="canvas">
  <section class="card card--front">
    <div class="wash wash--warm" role="img" aria-label="Watercolour floral wash in sepia, sand and olive tones"></div>
    <div class="pin-spot" role="img" aria-label="Awareness ribbon where the pin is attached"></div>
    <div class="letter">
      <p>Dear Friends</p>
      <p>Your support in attending<br>this memorial and celebration<br>of life means so much to us.</p>
      <p>Our loved one has touched<br>you in ways we may not<br>even recognize yet.</p>
      <p>We invite you to wear this<br>pin through your grieving<br>process, which we receive as<br>a symbol of your sympathy<br>and support of our loss.</p>
    </div>
    <div class="maker"><span class="maker__mark"></span><span>Kindred Rest</span></div>
  </section>

  <section class="card card--back">
    <div class="wash wash--cool" role="img" aria-label="Pale grey and cream watercolour floral wash"></div>
    <h2 class="message__title">Leave a message to the family</h2>
    <div class="message__lines">
      <div class="message__line"></div>
      <div class="message__line"></div>
      <div class="message__line"></div>
      <div class="message__line"></div>
      <div class="message__line"></div>
      <div class="message__line"></div>
      <div class="message__line"></div>
    </div>
    <div class="maker"><span class="maker__mark"></span><span>Kindred Rest</span></div>
  </section>
</main>
</body>
</html>
```